Cleaning Company and Staynest Tasks

Our London based company provides services for all things related to Staynest. Our main tasks are cleaning, checkins & linen. We are in need of a fresh new design that allows customers to book our services with ease.

The site must keep in mind that it will be primarily used on mobile and payment to be taken online.

What we require:

- Two pages designed, Home page (see Homepage doc) and Purchase Page (see flow chart)

Things we like:-

- We like mainly white and pastel based colours.
- Usage of vector style graphics through our the site to represent people & tasks.
- Shopping cart, with lots of images to select services
- Shopping cart that always has the pricing floating on the right
- Shopping cart that is wizard based.
- We like the usage of wonk characters on this site (for us probably angels)
http://www.tradelarks.com/pricing.php
- Slightly quirky design.

Sites we like:
http://vantageforge.com/ - bold action
https://www.mailorbit.com/ - a very playful design

TO AVOID WASTING TIME, INITIALLY DESIGN THE FRONT PAGE ONLY, IF WE LIKE YOUR HOME PAGE DESIGN THEM WE CAN SHORT LIST YOU INTO DESIGNING THE PAYMENT WIZARD PAGE

Target Market(s)

Young working professionals.

Industry/Entity Type

Cleaning Service

Contact Information for Business Card

Name: Rob Patel
Title: Senior Sales Representative
Tel: +44 (0) 777 4818 5096
Office: +44 (0) 207 413 6871
email: mh@fernhollowstays.co.uk
web: www.fernhollowstays.co.uk

Number of Pages Required

2 page

Font styles to use
Sans Serif

Colors
876aae
6b449b

Requirements
Must have
• - Two pages designed including home page and wizard to purchase services.
• - Usage of vector images.
Nice to have
• Angels to represent tasks
• We also like the colour yellow, the branding can be changed to suit this colour change.
Should not have
• A design that must not look like a Pagecraft standard Pagecraft theme.

```html
<!DOCTYPE html>
<html lang="en">
<head>
<meta charset="utf-8">
<title>fernhollowstays — Staynest services</title>
<link rel="stylesheet" href="https://fonts.googleapis.com/css2?family=Quicksand:wght@400;500;600&family=Lato:ital,wght@0,400;0,700;1,400&display=swap">
<style>
:root{
  --purple:#6b449b;
  --purple-soft:#876aae;
  --ink:#1b1b1b;
  --muted:#444;
  --topbar:#111;
  --navbar:#eeecea;
  --white:#fff;
  --line:#e4e0ea;
}
*{box-sizing:border-box;margin:0;padding:0}
html,body{width:1200px;height:2612px;overflow:hidden}
body{position:relative;background:var(--white);font-family:"Lato",Arial,sans-serif;color:var(--ink)}
.abs{position:absolute}
.heading{font-family:"Quicksand",Arial,sans-serif;font-weight:500;font-size:34px;color:var(--ink);text-align:center;width:1200px;left:0}
.heading span{color:var(--purple)}
.heading::after{content:"";display:block;width:56px;height:1px;background:var(--purple-soft);margin:12px auto 0}

/* top bar */
.topbar{top:0;left:0;width:1200px;height:42px;background:var(--topbar);color:var(--white);font-size:13px}
.topbar .item{position:absolute;top:13px;display:flex;align-items:center;gap:8px}
.social{position:absolute;display:flex;gap:16px}
.social i{display:block;width:12px;height:12px;border-radius:50%;background:var(--white)}

/* nav */
.navbar{top:42px;left:0;width:1200px;height:59px;background:var(--navbar)}
.brand{position:absolute;display:flex;align-items:center;gap:10px;font-family:"Quicksand",Arial,sans-serif;font-weight:400}
.brand .dot{width:30px;height:30px;border-radius:50%;background:var(--purple-soft)}
.navbar .brand{left:101px;top:13px;font-size:26px;color:var(--purple-soft)}
.nav a{position:absolute;top:20px;font-family:"Quicksand",Arial,sans-serif;font-size:16px;color:#333;text-decoration:none}
.nav a.active{color:var(--purple)}

/* hero */
.hero{top:101px;left:0;width:1200px;height:557px;background:linear-gradient(100deg,#c89b6e 0%,#e5cfaa 40%,#f3e4c8 65%,#8fa66a 90%)}
.hero .arrow{position:absolute;top:240px}
.hero-caption{position:absolute;left:0;bottom:0;width:1200px;height:57px;background:rgba(20,20,20,.72);color:var(--white);font-family:"Quicksand",Arial,sans-serif;font-weight:500;font-size:26px;text-align:center;line-height:57px}

/* services */
.lead{left:197px;width:808px;top:772px;text-align:center;font-size:12.5px;line-height:21px;color:var(--muted)}
.service h3{font-family:"Quicksand",Arial,sans-serif;font-weight:500;font-size:21px;color:var(--purple)}
.service p{font-size:12.5px;line-height:19px;color:var(--muted);margin-top:6px}
.service.left{text-align:right;width:300px;left:69px}
.service.right{text-align:left;width:300px;left:834px}

/* about */
.about{top:1106px;left:0;width:670px;height:428px;background:var(--purple);color:var(--white)}
.about h2{position:absolute;left:101px;top:40px;font-family:"Quicksand",Arial,sans-serif;font-weight:400;font-size:35px}
.about h2::after{content:"";display:block;width:48px;height:1px;background:var(--white);margin-top:10px}
.about p{position:absolute;left:101px;top:112px;width:545px;font-size:12.6px;line-height:22px}
.feature{position:absolute;top:266px;width:180px;text-align:center;font-weight:700;font-size:15px}
.feature .ring{width:84px;height:84px;border:3px solid var(--white);border-radius:50%;margin:0 auto 16px;display:flex;align-items:center;justify-content:center}
.about-photo{top:1106px;left:670px;width:530px;height:428px;background:linear-gradient(120deg,#b79a7b,#e8ded4 45%,#d45a78 70%,#8fae3b)}

/* how it works */
.how-photo{top:1679px;left:99px;width:521px;height:387px;background:linear-gradient(110deg,#d9d4cc,#8a7d6c 40%,#2f6e7a 65%,#c9d7d6)}
.step-icon{position:absolute;left:584px;width:72px;height:72px;border-radius:50%;background:#111;display:flex;align-items:center;justify-content:center}
.step-icon.first{background:var(--purple)}
.step-num{position:absolute;left:-2px;top:-4px;width:20px;height:20px;border-radius:50%;background:var(--purple-soft);color:var(--white);font-size:11px;text-align:center;line-height:16px;border:2px solid var(--white)}
.step{position:absolute;left:672px;width:420px}
.step h4{font-weight:400;font-size:16px;color:var(--ink)}
.step p{font-size:13px;line-height:21px;color:#777;margin-top:2px}

/* testimonial */
.avatar{top:2198px;left:101px;width:140px;height:140px;border-radius:50%;border:4px solid var(--purple);background:radial-gradient(circle at 50% 40%,#e7d5c6,#b9a89a)}
.avatar-tail{top:2318px;left:201px}
.quote-mark{top:2196px;left:286px}
.quote{top:2200px;left:286px;width:814px;font-style:italic;font-size:12.6px;line-height:28px;color:#333;text-indent:70px}
.quote-rule{top:2326px;left:282px;width:670px;height:1px;background:var(--line)}
.quote-name{top:2340px;left:284px;font-family:"Quicksand",Arial,sans-serif;font-size:16px;color:var(--purple)}
.pager{top:2344px;left:1046px;display:flex;gap:10px;align-items:center}
.pager i{display:block;width:8px;height:8px;border-radius:50%;background:#555}
.pager i.on{background:var(--purple);box-shadow:0 0 0 2px var(--white),0 0 0 3px var(--purple)}

/* footer */
.footer{top:2414px;left:0;width:1200px;height:155px;background:var(--purple);color:var(--white)}
.footer-links{position:absolute;left:101px;top:28px;display:flex;font-size:14px}
.footer-links a{color:var(--white);text-decoration:none}
.footer-links .sep{margin:0 28px}
.contact{position:absolute;top:88px;display:flex;gap:14px;font-size:12px;line-height:18px}
.contact .ring{width:32px;height:32px;border:2px solid var(--white);border-radius:50%;display:flex;align-items:center;justify-content:center;flex:none}
.contact b{font-weight:700}
.footer .brand{left:871px;top:64px;font-size:28px;color:#e4dcef}
.footer .brand .dot{background:#e4dcef}
.copybar{top:2569px;left:0;width:1200px;height:43px;background:var(--topbar);color:var(--white);font-size:12.5px}
.copybar .text{position:absolute;left:101px;top:14px}
.copybar .circles{position:absolute;left:926px;top:6px;display:flex;gap:11px}
.copybar .circles i{display:block;width:32px;height:32px;border:2px solid var(--white);border-radius:50%}
</style>
</head>
<body>

<header class="topbar abs">
  <div class="item" style="left:101px">
    <svg width="16" height="12" viewBox="0 0 16 12"><rect x="0" y="0" width="16" height="12" fill="#fff"/><path d="M0 0 L8 7 L16 0" stroke="#111" stroke-width="1.5" fill="none"/></svg>
    info@fernhollowstays.com
  </div>
  <div class="item" style="left:293px">
    <svg width="13" height="13" viewBox="0 0 24 24"><path fill="#fff" d="M6.6 10.8a15 15 0 006.6 6.6l2.2-2.2a1 1 0 011-.25 11.4 11.4 0 003.6.6 1 1 0 011 1V20a1 1 0 01-1 1A17 17 0 013 4a1 1 0 011-1h3.5a1 1 0 011 1c0 1.25.2 2.45.6 3.6a1 1 0 01-.25 1z"/></svg>
    020-555-0147
  </div>
  <div class="social" style="left:740px;top:15px"><i></i><i></i><i></i><i></i></div>
  <div class="item" style="left:1036px;font-size:14px">
    <svg width="16" height="16" viewBox="0 0 16 16"><path d="M6 2h8v12H6" stroke="#fff" stroke-width="1.6" fill="none"/><path d="M1 8h8M6 5l3 3-3 3" stroke="#fff" stroke-width="1.6" fill="none"/></svg>
    Login
  </div>
</header>

<nav class="navbar abs">
  <div class="brand"><span class="dot"></span>fernhollowstays</div>
  <div class="nav">
    <a class="active" style="left:427px">Home</a>
    <a style="left:512px">About Us</a>
    <a style="left:618px">Our Services</a>
    <a style="left:752px">News</a>
    <a style="left:833px">Useful Information</a>
    <a style="left:1015px">Contact Us</a>
  </div>
</nav>

<section class="hero abs" role="img" aria-label="Photo of a bright bedroom with a striped bed, wooden drawers and a desk by the window">
  <svg class="arrow" style="left:44px" width="20" height="40" viewBox="0 0 20 40"><path d="M16 2 L4 20 L16 38" stroke="#fff" stroke-width="2" fill="none"/></svg>
  <svg class="arrow" style="left:1136px" width="20" height="40" viewBox="0 0 20 40"><path d="M4 2 L16 20 L4 38" stroke="#fff" stroke-width="2" fill="none"/></svg>
  <div class="hero-caption">We are UK based firm Provides Services for all things Related to Staynest only</div>
</section>

<h2 class="heading abs" style="top:700px">Our <span>Services</span></h2>
<p class="lead abs">Duis autem vel eum iriure dolor in hendrerit in vulputate velit esse molestie consequat, vel illum dolore eu feugiat nulla facilisis at vero eros et accumsan et iusto odio dignissim qui blandit delenit augue duis dolore te feugait nulla facilisi.</p>

<svg class="abs" style="left:0;top:840px" width="1200" height="220" viewBox="0 0 1200 220">
  <g stroke="#6b449b" stroke-width="1.5" fill="none">
    <path d="M442 45 H560 V90"/>
    <path d="M442 181 H560 V140"/>
    <path d="M770 45 H640 V90"/>
    <path d="M770 181 H640 V140"/>
  </g>
  <g fill="#6b449b"><circle cx="442" cy="45" r="4"/><circle cx="442" cy="181" r="4"/><circle cx="770" cy="45" r="4"/><circle cx="770" cy="181" r="4"/></g>
  <circle cx="601" cy="113" r="61" fill="#6b449b"/>
  <circle cx="601" cy="113" r="20" fill="none" stroke="#fff" stroke-width="3"/>
  <g stroke="#111" stroke-width="2.2" fill="none">
    <rect x="392" y="28" width="28" height="34" rx="2"/><path d="M398 38h16M398 46h16M398 54h10"/>
    <path d="M776 52 L800 30 L824 52 M782 48 V66 H818 V48"/><path d="M793 56h14"/>
    <circle cx="407" cy="181" r="14"/><circle cx="407" cy="181" r="5"/>
    <circle cx="794" cy="168" r="8"/><path d="M780 196 Q794 176 808 196"/>
  </g>
</svg>

<div class="service left abs" style="top:848px"><h3>Staynest Tasks</h3><p>Duis autl vel eum iriure dolor in lkhe vulputa euismod tincidunt ut laoreet dolore magna.</p></div>
<div class="service right abs" style="top:848px"><h3>Domestic Cleaning</h3><p>Duis autl vel eum iriure dolor in lkhe vulput euismod tincidunt ut laoreet dolore magna.</p></div>
<div class="service left abs" style="top:976px"><h3>Staynest Management</h3><p>Duis autl vel eum iriure dolor in lkhe vulputa euismod tincidunt ut laoreet dolore magna.</p></div>
<div class="service right abs" style="top:976px"><h3>Handyman</h3><p>Duis autl vel eum iriure dolor in lkhe vulput euismod tincidunt ut laoreet dolore magna.</p></div>

<section class="about abs">
  <h2>About fernhollowstays</h2>
  <p>Lorem ipsum dolor sit amet, consectetuer adipiscing elit, sed diam nonummy nibh euismod tincidunt ut laoreet dolore magna aliquam erat volutpat. Ut wisi enim adminim veniam quis nostrud exerci tation ullamcorper suscipit lobortis nisl ut aliquip ex ea commodo consequ. Duis autem vel eum iriure dolor in hendrerit in vulputate velit esse molestie consequat, vel illum dolore eu feugiat nulla facilisis at vero eros et accumsan et iusto odio dignissim qui blandit praesent luptatum zzril delenit augue duis dolore te feugait nulla.</p>
  <div class="feature" style="left:93px">
    <div class="ring"><svg width="34" height="40" viewBox="0 0 34 40" fill="none" stroke="#fff" stroke-width="2.4"><path d="M4 2h18l8 8v28H4z"/><circle cx="17" cy="20" r="6"/><path d="M14 26l-2 8 5-3 5 3-2-8"/></svg></div>
    Trusted Professionals
  </div>
  <div class="feature" style="left:297px">
    <div class="ring"><svg width="40" height="40" viewBox="0 0 40 40" fill="none" stroke="#fff" stroke-width="2.4"><circle cx="20" cy="20" r="15"/><path d="M20 11v10l7 4"/></svg></div>
    Same-Day Availability
  </div>
  <div class="feature" style="left:502px">
    <div class="ring"><svg width="38" height="38" viewBox="0 0 38 38"><path fill="#fff" d="M4 16h7v18H4zM13 16l7-12c3 0 4 2 3 6l-1 4h10c2 0 3 2 3 4l-3 13c-.5 2-2 3-4 3H13z"/></svg></div>
    Our Guarantee
  </div>
</section>
<div class="about-photo abs" role="img" aria-label="Photo of a guest bedroom with a spotted bedspread, green throw and a wooden dresser"></div>

<h2 class="heading abs" style="top:1580px">How It <span>Works</span></h2>
<div class="how-photo abs" role="img" aria-label="Photo of a made bedroom with a wooden bed frame, blue and purple bedding and matching drawers"></div>

<div class="step-icon first" style="top:1699px"><span class="step-num">1</span>
  <svg width="32" height="32" viewBox="0 0 32 32" fill="none" stroke="#fff" stroke-width="2.2"><path d="M12 18V6a2 2 0 014 0v9l8 2v7l-4 6h-8l-5-8 3-2 2 3"/></svg></div>
<div class="step-icon" style="top:1788px"><span class="step-num">2</span>
  <svg width="32" height="32" viewBox="0 0 32 32" fill="none" stroke="#fff" stroke-width="2.2"><rect x="4" y="6" width="22" height="20" rx="2"/><path d="M4 12h22M10 3v6M20 3v6"/><circle cx="24" cy="24" r="6" fill="#111"/><path d="M24 21v3h2"/></svg></div>
<div class="step-icon" style="top:1875px"><span class="step-num">3</span>
  <svg width="34" height="30" viewBox="0 0 34 30" fill="none" stroke="#fff" stroke-width="2.2"><rect x="2" y="4" width="26" height="18" rx="2"/><path d="M8 10h10M8 15h6"/><rect x="22" y="16" width="10" height="10" fill="#111"/><path d="M24 16v-3a3 3 0 016 0v3"/></svg></div>
<div class="step-icon" style="top:1965px"><span class="step-num">4</span>
  <svg width="32" height="32" viewBox="0 0 32 32" fill="none" stroke="#fff" stroke-width="2.2"><circle cx="11" cy="7" r="3"/><path d="M11 11l3 9h9l3 7M14 15l-6 5 4 7M6 26h8"/></svg></div>

<div class="step" style="top:1708px"><h4>Select A Service</h4><p>Lorem ipsum dolor sit amet, consectetuer adipiscing elit, sed diam nonummy nibh</p></div>
<div class="step" style="top:1797px"><h4>Time &amp; Date You'd Like A Our Professional To Attend</h4><p>Lorem ipsum dolor sit amet, consectetuer adipiscing elit, sed diam nonummy nibh</p></div>
<div class="step" style="top:1885px"><h4>Pay Securely Online</h4><p>Lorem ipsum dolor sit amet, consectetuer adipiscing elit, sed diam nonummy nibh</p></div>
<div class="step" style="top:1975px"><h4>Sit Back, Relax And Wait For One Of Our Professionals</h4><p>Lorem ipsum dolor sit amet, consectetuer adipiscing elit, sed diam nonummy nibh</p></div>

<h2 class="heading abs" style="top:2113px">What Customer <span>Said</span></h2>
<div class="avatar abs" role="img" aria-label="Customer portrait photo"></div>
<svg class="avatar-tail abs" width="30" height="30" viewBox="0 0 30 30"><path d="M2 4 L26 26 L20 2 Z" fill="#fff" stroke="#6b449b" stroke-width="4" stroke-linejoin="round"/></svg>
<svg class="quote-mark abs" width="56" height="44" viewBox="0 0 56 44"><path fill="#d8d8d8" d="M2 44V24C2 10 8 3 22 1l2 6c-7 2-10 6-10 12h10v25zM32 44V24c0-14 6-21 20-23l2 6c-7 2-10 6-10 12h10v25z"/></svg>
<p class="quote abs">Lorem ipsum dolor smit amet, consectetuer adipiscing elitmk, sed amet diam nonummy nibh euismod tincidun nt ut laoreetml dolore magna aliquam erat volutpat. Ut wisi enim ad minim veniam, quis nostrud exer tationk ullamcorper suscipit lobortisk nisl utml aliqpi ex ea commodo consequat. Duis autem vel eumk iriure dolor inj hendrerit inn vulputate velit esse molestiemo consequat, velhki illumn gnol dolore eu feugiat nulla facilisis at vero eros dignissim.</p>
<div class="quote-rule abs"></div>
<div class="quote-name abs">- Mr. Tomas Elwin</div>
<div class="pager abs"><i class="on"></i><i></i><i></i></div>

<footer class="footer abs">
  <div class="footer-links">
    <a>Home</a><span class="sep">|</span><a>About Us</a><span class="sep">|</span><a>Our Services</a><span class="sep">|</span><a>News</a><span class="sep">|</span><a>Useful Information</a><span class="sep">|</span><a>Contact Us</a>
  </div>
  <div class="contact" style="left:99px">
    <span class="ring"><svg width="14" height="16" viewBox="0 0 14 18"><path fill="#fff" d="M7 0a7 7 0 017 7c0 5-7 11-7 11S0 12 0 7a7 7 0 017-7zm0 4a3 3 0 100 6 3 3 0 000-6z"/></svg></span>
    <div><b>fernhollowstays</b><br>48 Wickham Row, Larchfield - LN4 7QE</div>
  </div>
  <div class="contact" style="left:445px">
    <span class="ring"><svg width="14" height="14" viewBox="0 0 24 24"><path fill="#fff" d="M6.6 10.8a15 15 0 006.6 6.6l2.2-2.2a1 1 0 011-.25 11.4 11.4 0 003.6.6 1 1 0 011 1V20a1 1 0 01-1 1A17 17 0 013 4a1 1 0 011-1h3.5a1 1 0 011 1c0 1.25.2 2.45.6 3.6a1 1 0 01-.25 1z"/></svg></span>
    <div><b>Call Us :</b><br>020-555-0147</div>
  </div>
  <div class="contact" style="left:647px">
    <span class="ring"><svg width="14" height="11" viewBox="0 0 16 12"><rect width="16" height="12" fill="#fff"/><path d="M0 0 L8 7 L16 0" stroke="#6b449b" stroke-width="1.5" fill="none"/></svg></span>
    <div><b>Email Us :</b><br>info@fernhollowstays.com</div>
  </div>
  <div class="brand"><span class="dot"></span>fernhollowstays</div>
</footer>

<div class="copybar abs">
  <div class="text">Copyright © 2017 fernhollowstays. All Rights Reserved.</div>
  <div class="circles"><i></i><i></i><i></i><i></i></div>
</div>

</body>
</html>
```